Advertising Portal Needs eBrochure

Hi Crowders! Our advertising portal, which focus on the new launches property, needs an online brochure to promote to potential advertisers the benefits of advertising their projects with us. These advertisers will be mainly real estate developers and agencies.

WHAT WE LOOKING FOR
We do not want over-fanciful designs that makes the content hard to read. The use of illustrations and graphics/symbols related to covered topics are encouraged. The overall design should portrait our advertising efficiency through online and social media means. Our website - www.brightkeyhomes.sg.

For draft purposes, just do up the front page, back page, and few inner pages, preferably to include one illustration chart (either on page 7/8). Size wise probably A5 portrait or landscape, for future printing into a booklet.

WORK COMPLETION AND PAYMENT
The $500 stated here is 50% of the payment. Upon getting a desired draft design, we will need you to work on the full content with slight amendments along the way. Once done, we will be paying the balance $500, and we will need the pdf file as well as the work file.

Let your design juice flow, and hope we can work with you!
Updates

Hi Crowders! Thank you for your submissions. We are closing the project as we've decided on a design. It's a pity we can only select one design, as there are a number of good works. Hope we will have a chance to work together on our upcoming projects. Cheers =)

Target Market(s)

Real estate developers, real estate agencies, and perhaps to an extent, individual property sales agent.

Industry/Entity Type

Advertising

Requirements
Should not have
• We prefer not to have much real people kind of stock images. Try not to use images from our portal as we do not have the ownerships. Instead, you can use stock images of property developments artist impression that gives a similar feel.

```html
<!DOCTYPE html>
<html lang="en">
<head>
<meta charset="utf-8">
<title>Bright Key Homes – Marketing eBrochure Spread</title>
<link rel="stylesheet" href="https://fonts.googleapis.com/css2?family=Exo+2:wght@400;500;600;700&display=swap">
<style>
:root{
  --backdrop:#e9e7e3;
  --blue-top:#2fb0ec;
  --blue-bottom:#1689d2;
  --green-top:#4cbd4d;
  --green-bottom:#2fa03c;
  --ink:#ffffff;
  --accent:#f6e23a;
  --orange:#ef8a1c;
  --lime:#a6cc2e;
  --magenta:#e3197e;
  --navy:#1f3d74;
  --slate:#5c6f86;
}
*{margin:0;padding:0;box-sizing:border-box}
html,body{width:1200px;height:540px;overflow:hidden;background:var(--backdrop)}
body{font-family:"Exo 2",sans-serif;color:var(--ink);position:relative}
.spread{position:absolute;left:30px;top:35px;width:1140px;height:470px;display:flex;box-shadow:0 6px 18px rgba(0,0,0,.25)}
.page{position:relative;width:570px;height:470px;overflow:hidden}
.page--left{background:linear-gradient(180deg,var(--blue-top),var(--blue-bottom))}
.page--right{background:linear-gradient(180deg,var(--green-top),var(--green-bottom))}
.section-title{position:absolute;font-weight:700;font-size:13px;letter-spacing:.6px;text-transform:uppercase;white-space:nowrap}
.body-copy{position:absolute;font-size:8px;line-height:1.2;font-style:italic;font-weight:500}
.body-copy p{margin-bottom:6px}
.body-copy ul{margin-left:14px}
.mini-title{position:absolute;font-size:8.5px;font-weight:700;color:var(--accent);white-space:nowrap}
.placeholder{position:absolute;border-radius:2px}
.ad-card{left:356px;top:40px;width:136px;height:160px;background:linear-gradient(180deg,#ffffff,#dfe6ee);box-shadow:3px 4px 8px rgba(0,0,0,.35)}
.ad-card__label{position:absolute;left:366px;top:24px;font-size:8.5px;font-weight:700;text-transform:uppercase;white-space:nowrap}
.pie{position:absolute;left:20px;top:262px}
.chart-caption{position:absolute;left:92px;top:440px;font-size:10.5px;font-weight:700;color:var(--accent)}
.reach{position:absolute;left:280px;top:236px;font-size:10px;font-weight:600;line-height:1.25}
.reach b{color:var(--accent);font-weight:700}
.age-chart{position:absolute;left:262px;top:282px}
.monitor{left:240px;top:36px;width:150px;height:110px;background:linear-gradient(180deg,#cfd8df,#7f8c96)}
.newspaper{left:398px;top:54px;width:150px;height:80px;background:linear-gradient(180deg,#f5f5f5,#d9d9d9)}
.compare-caption{position:absolute;left:244px;top:160px;width:310px;font-size:7.4px;font-weight:600;color:var(--accent)}
.flow{position:absolute;left:234px;top:258px}
.flow-title{position:absolute;left:240px;top:246px;font-size:8.5px;font-weight:700;color:var(--accent);white-space:nowrap}
.project-word{position:absolute;left:462px;top:324px;font-size:15px;font-weight:700;color:var(--accent);text-align:center;line-height:1.1}
.folder{left:470px;top:368px;width:56px;height:42px;background:linear-gradient(180deg,#f7d35a,#e1a322)}
.illustration-caption{position:absolute;left:350px;top:430px;font-size:8px;font-weight:600;color:var(--accent)}
</style>
</head>
<body>
<main class="spread">
  <section class="page page--left">
    <h2 class="section-title" style="left:60px;top:30px">Effective Circlebook Marketing</h2>
    <div class="body-copy" style="left:30px;top:56px;width:310px">
      <p>Another very important platform when it comes to online marketing, is Circlebook. Recognized as the most popular social media, with growing number of users and increase in average time spent per user, Circlebook marketing is increasingly popular, and if done right, is way more effective compared to traditional marketing methods.</p>
      <p>Considering distribution of 100,000 flyers, it will easily cost you more than $10,000 for design, printing and distribution.</p>
      <p>However, with our Circlebook marketing campaign, it will be much more effective in the following ways:</p>
      <ul>
        <li>Reach out to the same number of consumers at a much, much lower cost</li>
        <li>Targeted consumers, based on age/gender/interest etc.</li>
        <li>The advertisement will link directly to your project webpage for better reference</li>
        <li>Consumers are more likely to respond to the advertisement</li>
      </ul>
    </div>

    <span class="ad-card__label">Sample Circlebook Ad</span>
    <div class="placeholder ad-card" role="img" aria-label="Sample social media ad for Meridian Towers with an artist impression of the condominium towers"></div>

    <svg class="pie" width="270" height="176" viewBox="0 0 270 176" aria-label="Engagement breakdown pie chart">
      <g transform="translate(40,14)">
        <path d="M90 80 L102.5 9.1 A72 72 0 1 1 20.2 97.4 Z" fill="var(--orange)"/>
        <path d="M90 80 L20.2 97.4 A72 72 0 0 1 32.5 36.7 Z" fill="var(--lime)"/>
        <path d="M90 80 L32.5 36.7 A72 72 0 0 1 35.7 32.8 Z" fill="#7fd0f0"/>
        <path d="M90 80 L35.7 32.8 A72 72 0 0 1 98.8 8.5 Z" fill="var(--magenta)"/>
        <path d="M90 80 L98.8 8.5 A72 72 0 0 1 102.5 9.1 Z" fill="#c4e04a"/>
      </g>
      <g stroke="#fff" stroke-width=".6" fill="none">
        <path d="M112 30 L108 20"/>
        <path d="M140 24 L150 10"/>
        <path d="M74 50 L60 46"/>
        <path d="M66 112 L56 112"/>
        <path d="M200 102 L206 102"/>
      </g>
      <g fill="#fff" font-size="6.5" font-family="Exo 2, sans-serif">
        <text x="78" y="17">Post Likes: <tspan fill="var(--accent)">286</tspan></text>
        <text x="152" y="11">Shares: <tspan fill="var(--accent)">11</tspan></text>
        <text x="4" y="46">Page Likes: <tspan fill="var(--accent)">21</tspan></text>
        <text x="0" y="114">Link Clicks: <tspan fill="var(--accent)">261</tspan></text>
        <text x="208" y="104">Photo Clicks: <tspan fill="var(--accent)">1,253</tspan></text>
      </g>
    </svg>
    <span class="chart-caption">Engagement Breakdown</span>

    <div class="reach">
      Active From: 01/04/2014 to 07/04/2014<br>
      <b>89,088</b> people seen your ad<br>
      <b>1,750</b> people engaged your ad
    </div>

    <svg class="age-chart" width="300" height="160" viewBox="0 0 300 160" aria-label="Audience by age and gender">
      <g font-family="Exo 2, sans-serif" font-weight="700">
        <circle cx="72" cy="18" r="6" fill="var(--navy)"/>
        <text x="84" y="22" font-size="10" fill="var(--accent)">67,1%</text>
        <circle cx="146" cy="18" r="6" fill="var(--magenta)"/>
        <text x="158" y="22" font-size="10" fill="var(--accent)">32,9%</text>

        <line x1="8" y1="136" x2="292" y2="136" stroke="var(--slate)" stroke-width="1.5"/>
        <g fill="#fff" stroke="var(--slate)" stroke-width="1.4">
          <circle cx="14" cy="118" r="3"/><circle cx="56" cy="118" r="3"/>
          <circle cx="238" cy="118" r="3"/><circle cx="282" cy="118" r="3"/>
        </g>
        <g fill="var(--magenta)">
          <circle cx="14" cy="136" r="2.5"/><circle cx="56" cy="136" r="2.5"/><circle cx="104" cy="136" r="2.5"/>
          <circle cx="152" cy="136" r="2.5"/><circle cx="196" cy="136" r="2.5"/><circle cx="238" cy="136" r="2.5"/><circle cx="282" cy="136" r="2.5"/>
        </g>
        <rect x="92" y="70" width="12" height="62" rx="4" fill="var(--navy)"/>
        <rect x="106" y="102" width="12" height="30" rx="4" fill="var(--magenta)"/>
        <rect x="140" y="118" width="12" height="14" rx="4" fill="var(--navy)"/>
        <rect x="154" y="110" width="12" height="22" rx="4" fill="var(--magenta)"/>
        <rect x="186" y="124" width="10" height="8" rx="3" fill="var(--navy)"/>
        <rect x="198" y="128" width="10" height="4" rx="2" fill="var(--magenta)"/>

        <g font-size="8.5" fill="#fff">
          <rect x="84" y="40" width="22" height="14" fill="var(--navy)"/><text x="87" y="50">768</text>
          <rect x="108" y="40" width="22" height="14" fill="var(--magenta)"/><text x="111" y="50">368</text>
          <rect x="132" y="54" width="22" height="14" fill="var(--navy)"/><text x="135" y="64">158</text>
          <rect x="156" y="54" width="22" height="14" fill="var(--magenta)"/><text x="159" y="64">288</text>
          <rect x="178" y="70" width="18" height="14" fill="var(--navy)"/><text x="182" y="80">84</text>
          <rect x="198" y="70" width="18" height="14" fill="var(--magenta)"/><text x="202" y="80">32</text>
        </g>
        <g font-size="8" font-weight="600" fill="var(--accent)">
          <text x="2" y="150">13-17</text><text x="44" y="150">18-24</text><text x="92" y="150">25-34</text>
          <text x="140" y="150">35-44</text><text x="184" y="150">45-54</text><text x="226" y="150">55-64</text><text x="274" y="150">65+</text>
        </g>
      </g>
    </svg>
  </section>

  <section class="page page--right">
    <h2 class="section-title" style="left:28px;top:30px">Harbour Time Exposure</h2>
    <div class="body-copy" style="left:28px;top:52px;width:204px">
      <p>While online marketing is slowly taking over printed ads, looking for property from Harbour Times is still a common practice by many consumers. The viewership is enormous, but how do you make your ad stands out and get your targeted buyers to pay more attention to your ad at a reasonable price?</p>
      <p>As such, we will put together a periodical ad on Harbour Times for you to feature your project. This ad will consolidate the new property launches in one full-color, prominent advertisement, so that buyers looking for new property will definitely take notice of this ad, and thus, your project featured with us will receive more attention as well, as compared to cluttering with the other advertisements in other sections.</p>
    </div>
    <span class="mini-title" style="left:246px;top:20px">Sample Harbour Times Ad</span>
    <div class="placeholder monitor" role="img" aria-label="Desktop monitor showing a full-colour new launches property ad"></div>
    <div class="placeholder newspaper" role="img" aria-label="Cluttered newspaper classifieds page for comparison"></div>
    <span class="compare-caption">Compare these 2 ads. Which one gets better attention for a buyer looking for new launches property?</span>

    <h2 class="section-title" style="left:28px;top:230px">Email Blasting</h2>
    <div class="body-copy" style="left:28px;top:252px;width:196px">
      <p>Want immediate attention for a new launch project? A promotion? A Re-launch? Or project coming to completion? Consumers are always interested with such events. Let us help you to spread this to public by notifying our subscribers, as well as local agents, on such important updates through our emails blasting service.</p>
      <p>How is it different from sending your own? Well, beside avoiding the hassle - a trusted name, recognized server, and a well-designed newsletter - will better catch the recipients attention, less likely to end in spam, and our targeted recipients are consumers with genuine interest and our subscribers numbers are growing fast.</p>
    </div>

    <span class="flow-title">How Our Marketing Campaigns Boost Your Project Awareness</span>
    <svg class="flow" width="220" height="170" viewBox="0 0 220 170" aria-label="Marketing channels flowing to your project">
      <defs>
        <linearGradient id="arrow-fade" x1="0" x2="1">
          <stop offset="0" stop-color="#fff" stop-opacity="0"/>
          <stop offset="1" stop-color="#fff" stop-opacity=".9"/>
        </linearGradient>
      </defs>
      <g font-family="Exo 2, sans-serif" font-weight="700" font-size="10" fill="var(--navy)">
        <rect x="6" y="22" width="44" height="40" rx="6" fill="#fff"/>
        <text x="28" y="46" text-anchor="middle">Seekly</text>
        <rect x="6" y="74" width="44" height="40" rx="6" fill="#fff"/>
        <text x="28" y="98" text-anchor="middle" font-size="8">Circlebook</text>
        <rect x="6" y="126" width="44" height="40" rx="6" fill="#fff"/>
        <text x="28" y="150" text-anchor="middle">HT</text>
      </g>
      <g fill="url(#arrow-fade)">
        <path d="M60 44 H196 V38 L210 48 L196 58 V52 H60 Z"/>
        <path d="M60 96 H196 V90 L210 100 L196 110 V104 H60 Z"/>
        <path d="M60 148 H196 V142 L210 152 L196 162 V156 H60 Z"/>
      </g>
      <g font-family="Exo 2, sans-serif" font-size="6.5" fill="#fff">
        <text x="68" y="26">Tens of thousands of genuine property</text>
        <text x="68" y="33">searchers monthly</text>
        <text x="68" y="78">60,000 to 100,000 targeted consumers</text>
        <text x="68" y="85">per campaign</text>
        <text x="68" y="135">Hundreds of thousands of eyeballs</text>
      </g>
    </svg>
    <div class="project-word">YOUR<br>PROJECT</div>
    <div class="placeholder folder" role="img" aria-label="Open project folder illustration"></div>
    <span class="illustration-caption">Illustration 1: Active Marketing</span>
  </section>
</main>
</body>
</html>
```